Letterhead Design Needed for Real Estate Office

We are a boutique real estate agency focused on property management. We need a letter head which is professional looking and include the following information:

Logo
ABN Number
Address
Postal Address
Phone
Fax
Mobile
Email
Website

Please note that the PLVAQT logo can not be changed and must be positioned at the bottom right corner.

Please find attached the existing letterhead design for all the required elements.

Target Market(s)

Letterhead mostly used for service of notices, business letters, clients communication

Industry/Entity Type

Boutique

Colors

Designer to choose colors to be used in the design.

Requirements
Must have
• Logo

```html
<!DOCTYPE html>
<html lang="en">
<head>
<meta charset="utf-8">
<title>Meridian Partners Letterhead</title>
<link href="https://fonts.googleapis.com/css2?family=Noto+Sans:wght@400;600&display=swap" rel="stylesheet">
<style>
  :root {
    --backdrop: #bdbdbd;
    --paper: #ffffff;
    --ink: #4f4f4f;
    --ink-soft: #5e5e5e;
    --brand-green: #6aa527;
    --brand-dark: #3a3a3a;
    --member-blue: #1c5aa0;
    --facet: rgba(0, 0, 0, 0.035);
  }
  * { box-sizing: border-box; margin: 0; padding: 0; }
  html, body { width: 1200px; height: 900px; overflow: hidden; }
  body {
    background: var(--backdrop);
    font-family: "Noto Sans", Verdana, sans-serif;
    color: var(--ink);
    position: relative;
  }
  .sheet {
    position: absolute;
    top: 93px;
    width: 505px;
    height: 712px;
    background: var(--paper);
    overflow: hidden;
  }
  .sheet--letter { left: 80px; }
  .sheet--blank { left: 615px; }
  .backdrop-facets {
    position: absolute;
    inset: 0 0 0 0;
    background: linear-gradient(135deg, transparent 30%, var(--facet) 55%, transparent 80%);
  }
  .brand {
    position: absolute;
    left: 25px;
    top: 40px;
    display: flex;
    align-items: center;
    gap: 9px;
  }
  .brand__square {
    width: 30px;
    height: 30px;
    background: var(--brand-green);
  }
  .brand__name {
    font-size: 16px;
    font-weight: 600;
    letter-spacing: 0.5px;
    color: var(--brand-dark);
  }
  .letter-body {
    position: absolute;
    left: 20px;
    top: 120px;
    width: 465px;
    font-size: 8.4px;
    line-height: 11.8px;
    letter-spacing: 0.35px;
    color: var(--ink-soft);
    text-align: justify;
  }
  .letter-body p { margin-bottom: 12px; }
  .letter-body .signoff { margin-top: 18px; }
  .footer-details {
    position: absolute;
    left: 25px;
    top: 654px;
    display: flex;
    font-size: 5.6px;
    line-height: 7.5px;
    color: var(--ink);
  }
  .footer-details__address { width: 104px; }
  .footer-details__rule {
    width: 1px;
    height: 45px;
    background: var(--brand-green);
    margin: -3px 15px 0 0;
  }
  .footer-details__contact strong { font-weight: 600; }
  .member-mark {
    position: absolute;
    right: 26px;
    top: 660px;
    display: flex;
    align-items: center;
    gap: 6px;
  }
  .member-mark__square {
    width: 14px;
    height: 14px;
    background: var(--member-blue);
  }
  .member-mark__name {
    font-size: 19px;
    font-weight: 600;
    color: var(--member-blue);
    letter-spacing: -0.3px;
  }
</style>
</head>
<body>

  <section class="sheet sheet--letter">
    <div class="backdrop-facets" role="img" aria-label="Faint large brand facet decoration"></div>
    <div class="brand">
      <span class="brand__square"></span>
      <span class="brand__name">MERIDIAN PARTNERS</span>
    </div>
    <div class="letter-body">
      <p>Lorem ipsum dolor sit amet, consectetur adipisicing elit, sed do eiusmod tempor incididunt ut labore et dolore magna aliqua. Ut enim ad minim veniam, quis nostrud exercitation ullamco laboris nisi ut aliquip ex ea commodo consequat. Duis aute irure dolor in reprehenderit in voluptate velit esse cillum dolore eu fugiat nulla pariatur. Excepteur sint occaecat cupidatat non proident, sunt in culpa qui officia deserunt mollit anim id est laborumLorem ipsum dolor sit amet, consectetur adipisicing elit, sed do eiusmod tempor incididunt ut labore et dolore magna aliqua. Ut enim ad minim veniam, quis nostrud exercitation ullamco laboris nisi ut aliquip ex ea commodo consequat. Duis aute irure dolor in reprehenderit in voluptate velit esse cillum dolore eu fugiat nulla pariatur. Excepteur sint occaecat cupidatat non proident, sunt in culpa qui officia deserunt mollit anim id est laborum.</p>
      <p>Lorem ipsum dolor sit amet, consectetur adipisicing elit, sed do eiusmod tempor incididunt ut labore et dolore magna aliqua. Ut enim ad minim veniam, quis nostrud exercitation ullamco laboris nisi ut aliquip ex ea commodo consequat. Duis aute irure dolor in reprehenderit in voluptate velit esse cillum dolore eu fugiat nulla pariatur. Excepteur sint occaecat cupidatat non proident, sunt in culpa qui officia deserunt mollit anim id est laborum.</p>
      <p>Lorem ipsum dolor sit amet, consectetur adipisicing elit, sed do eiusmod tempor incididunt ut labore et dolore magna aliqua. Ut enim ad minim veniam, quis nostrud exercitation ullamco laboris nisi ut aliquip ex ea commodo consequat. Duis aute irure dolor in reprehenderit in voluptate velit esse cillum dolore eu fugiat nulla pariatur. Excepteur sint occaecat cupidatat non proident, sunt in culpa qui officia deserunt mollit anim id est laborum.</p>
      <p>Lorem ipsum dolor sit amet, consectetur adipisicing elit, sed do eiusmod tempor incididunt ut labore et dolore magna aliqua. Ut enim ad minim veniam, quis nostrud exercitation ullamco laboris nisi ut aliquip ex ea commodo consequat. Duis aute irure dolor in reprehenderit in voluptate velit esse cillum dolore eu fugiat nulla pariatur. Excepteur sint occaecat cupidatat non proident, sunt in culpa qui officia deserunt mollit anim id est laborumLorem ipsum dolor sit amet, consectetur adipisicing elit, sed do eiusmod tempor incididunt ut labore et dolore magna aliqua. Ut enim ad minim veniam, quis nostrud exercitation ullamco laboris nisi ut aliquip ex ea commodo consequat. Duis aute irure dolor in reprehenderit in voluptate velit esse cillum dolore eu fugiat nulla pariatur. Excepteur sint occaecat cupidatat non proident, sunt in culpa qui officia deserunt mollit anim id est laborum.</p>
      <p>Lorem ipsum dolor sit amet, consectetur adipisicing elit, sed do eiusmod tempor incididunt ut labore et dolore magna aliqua. Ut enim ad minim veniam, quis nostrud exercitation ullamco laboris nisi ut aliquip ex ea commodo consequat. Duis aute irure dolor in reprehenderit in voluptate velit esse cillum dolore eu fugiat nulla pariatur. Excepteur sint occaecat cupidatat non proident, sunt in culpa qui officia deserunt mollit anim id est laborum.</p>
      <p class="signoff">Managing Consultant</p>
    </div>
    <div class="footer-details">
      <div class="footer-details__address">ABN 12 345 678 901<br>Shop 12B 100-120<br>Harbour Street Lindfield<br>NSW 2070 AUSTRALIA<br>PO BOX 410 Lindfield NSW 2070</div>
      <div class="footer-details__rule"></div>
      <div class="footer-details__contact">M: 0400 123 456<br>P: 9100 2200<br>F: 9100 2201<br>E: info@mdpre.cc<br><strong>www.mdpre.cc</strong></div>
    </div>
    <div class="member-mark">
      <span class="member-mark__square"></span>
      <span class="member-mark__name">PLVAQT</span>
    </div>
  </section>

  <section class="sheet sheet--blank">
    <div class="backdrop-facets" role="img" aria-label="Faint large brand facet decoration"></div>
    <div class="brand">
      <span class="brand__square"></span>
      <span class="brand__name">MERIDIAN PARTNERS</span>
    </div>
    <div class="footer-details">
      <div class="footer-details__address">ABN 12 345 678 901<br>Shop 12B 100-120<br>Harbour Street Lindfield<br>NSW 2070 AUSTRALIA<br>PO BOX 410 Lindfield NSW 2070</div>
      <div class="footer-details__rule"></div>
      <div class="footer-details__contact">M: 0400 123 456<br>P: 9100 2200<br>F: 9100 2201<br>E: info@mdpre.cc<br><strong>www.mdpre.cc</strong></div>
    </div>
    <div class="member-mark">
      <span class="member-mark__square"></span>
      <span class="member-mark__name">PLVAQT</span>
    </div>
  </section>

</body>
</html>
```